Back Pain

Need a flyer similar to the attached draft. This is to be handed out to prospective patients. Note that Sketch Hive has already designed the logo. If you need a copy please contact me

```html
<!DOCTYPE html>
<html lang="en">
<head>
<meta charset="utf-8">
<title>Spine Ease Clinic – Tech Neck Flyer</title>
<link rel="stylesheet" href="https://fonts.googleapis.com/css2?family=Montserrat:wght@500;600;700&family=Oswald:wght@400;500;700&display=swap">
<style>
  :root {
    --black: #000000;
    --white: #ffffff;
    --ink: #111111;
    --blue: #0a72c0;
    --blue-deep: #0b6db8;
    --teal: #0aa2c4;
    --teal-dark: #0785a3;
    --green: #8dc63f;
    --grey-ring: #e4e4e4;
    --brand-gradient: linear-gradient(90deg, var(--green) 0%, var(--blue) 100%);
  }
  * { margin: 0; padding: 0; box-sizing: border-box; }
  html, body { width: 960px; height: 1200px; overflow: hidden; background: var(--white); }
  .flyer {
    position: relative; width: 960px; height: 1200px; overflow: hidden;
    background: var(--white); font-family: "Oswald", sans-serif; color: var(--ink);
  }

  /* Header */
  .masthead { position: absolute; left: 0; top: 0; width: 960px; height: 206px; background: var(--black); }
  .masthead__stripe { position: absolute; left: 0; top: 206px; width: 960px; height: 12px; background: var(--brand-gradient); }
  .brand { position: absolute; left: 95px; top: 48px; display: flex; align-items: center; gap: 36px; }
  .brand__mark { width: 126px; height: 126px; border-radius: 50%; background: var(--teal); flex: none; }
  .brand__text { font-family: "Montserrat", sans-serif; color: var(--teal); }
  .brand__name { font-weight: 600; font-size: 52px; letter-spacing: -1px; line-height: 1; white-space: nowrap; }
  .brand__tagline { font-weight: 600; font-size: 21px; letter-spacing: 6.4px; margin-top: 8px; white-space: nowrap; }

  /* Illustration */
  .figure-art {
    position: absolute; left: 70px; top: 249px; width: 238px; height: 631px;
    border-radius: 120px 120px 30px 30px;
    background: linear-gradient(180deg, #5a2446 0%, #2f4a75 30%, #2c1c35 60%, #d6294e 100%);
    opacity: .9;
  }

  /* Symptoms */
  .symptoms { list-style: none; }
  .symptom {
    position: absolute; left: 213px; height: 37px; border-radius: 0 20px 20px 0;
    background: linear-gradient(90deg, rgba(10,114,192,0) 0%, rgba(10,114,192,.55) 35%, var(--blue) 68%);
    color: var(--white); font-weight: 700; font-size: 24px; line-height: 37px; padding-left: 102px;
    white-space: nowrap;
  }

  /* Chart */
  .chart-heading { position: absolute; left: 551px; top: 272px; font-size: 22px; line-height: 31px; font-weight: 400; white-space: nowrap; }
  .accent { color: var(--blue); font-weight: 700; }
  .bold { font-weight: 700; }
  .chart { position: absolute; left: 540px; top: 330px; }
  .chart-caption { position: absolute; left: 551px; top: 500px; font-size: 22px; white-space: nowrap; }
  .chart-axis-label {
    position: absolute; left: 882px; top: 500px; transform: rotate(-90deg); transform-origin: 0 0;
    font-size: 19px; white-space: nowrap; width: 210px;
  }

  /* Screen time */
  .pie { position: absolute; left: 481px; top: 573px; }
  .screen-time { position: absolute; left: 611px; top: 572px; }
  .screen-time__lead { font-size: 25px; line-height: 30px; white-space: nowrap; }
  .screen-time__hours {
    margin-top: 5px; width: 296px; height: 46px; background: var(--blue-deep); color: var(--white);
    font-weight: 700; font-size: 31px; line-height: 46px; text-align: center; letter-spacing: .5px;
  }
  .screen-time__tail { margin-top: 4px; font-size: 25px; line-height: 30px; white-space: nowrap; }

  /* Message */
  .message { position: absolute; left: 342px; top: 712px; font-size: 32px; line-height: 45px; font-weight: 400; white-space: nowrap; }

  /* Footer */
  .doctor-band {
    position: absolute; left: 0; top: 915px; width: 960px; height: 71px; background: var(--brand-gradient);
    color: var(--white); font-family: "Montserrat", sans-serif; font-weight: 700; font-size: 42px; line-height: 71px; text-align: center;
  }
  .location { position: absolute; left: 0; top: 994px; width: 960px; text-align: center; font-family: "Montserrat", sans-serif; font-weight: 600; font-size: 21px; }
  .offer {
    position: absolute; left: 174px; top: 1029px; width: 612px; height: 61px; background: var(--green);
    border: 1.5px dashed var(--blue); border-radius: 4px; color: var(--white);
    font-weight: 700; font-size: 42px; line-height: 58px; text-align: center;
  }
  .booking { position: absolute; left: 0; top: 1100px; width: 960px; text-align: center; font-family: "Montserrat", sans-serif; font-weight: 600; font-size: 21px; white-space: nowrap; }
  .booking__url { color: var(--blue); font-weight: 700; }
  .option {
    position: absolute; left: 176px; top: 1134px; width: 608px; height: 41px; border: 1.5px dashed var(--blue);
    font-family: "Montserrat", sans-serif; font-weight: 600; font-size: 21px; letter-spacing: 5px; line-height: 38px; text-align: center;
  }
  .option__key { color: var(--blue); font-weight: 700; }
</style>
</head>
<body>
<main class="flyer">
  <header class="masthead">
    <div class="brand">
      <span class="brand__mark" aria-hidden="true"></span>
      <div class="brand__text">
        <div class="brand__name">SPINE EASE CLINIC</div>
        <div class="brand__tagline">DR SAM WHITFORD - CHIROPRACTOR</div>
      </div>
    </div>
  </header>
  <div class="masthead__stripe"></div>

  <div class="figure-art" role="img" aria-label="Illustration of a man walking while looking down at his phone"></div>

  <ul class="symptoms">
    <li class="symptom" style="top:277px;width:254px">HEADCHES</li>
    <li class="symptom" style="top:323px;width:254px">NECK PAIN</li>
    <li class="symptom" style="top:370px;width:291px">SHOULDER PAIN</li>
    <li class="symptom" style="top:418px;width:254px">BACK PAIN</li>
    <li class="symptom" style="top:484px;width:315px">ARM &amp; HAND PAIN</li>
    <li class="symptom" style="top:531px;width:254px">SCIATICA</li>
  </ul>

  <p class="chart-heading">AT THE <span class="accent">HEAD TILTS</span> FORWARD.<br>MORE FORCE IS PLACED ON THE SPINE</p>

  <svg class="chart" width="330" height="170" viewBox="0 0 330 170" role="img" aria-label="Bar chart: pressure on spine of 12, 27, 40, 49 and 60 lbs at 0, 15, 30, 45 and 60 degrees of head tilt">
    <rect x="15" y="66" width="36" height="40" rx="8" fill="#8a3b58" role="img" aria-label="Small head icon"/>
    <g font-family="Oswald, sans-serif" font-weight="700" font-size="21" fill="#ffffff" text-anchor="middle">
      <polygon points="13,142 25,120 68,120 68,142" fill="#0aa2c4"/><text x="47" y="139">12</text>
      <polygon points="75,142 75,96 87,84 130,84 130,142" fill="#0aa2c4"/><polygon points="75,96 87,84 87,142 75,142" fill="#0785a3"/><text x="108" y="124">27</text>
      <polygon points="138,142 138,71 150,59 193,59 193,142" fill="#0aa2c4"/><polygon points="138,71 150,59 150,142 138,142" fill="#0785a3"/><text x="171" y="101">40</text>
      <polygon points="200,142 200,51 212,39 255,39 255,142" fill="#0aa2c4"/><polygon points="200,51 212,39 212,142 200,142" fill="#0785a3"/><text x="233" y="80">49</text>
      <polygon points="263,142 263,26 275,14 318,14 318,142" fill="#0aa2c4"/><polygon points="263,26 275,14 275,142 263,142" fill="#0785a3"/><text x="296" y="57">60</text>
    </g>
    <g font-family="Oswald, sans-serif" font-size="15" fill="#111" text-anchor="middle">
      <text x="33" y="162">0°</text><text x="96" y="162">15°</text><text x="159" y="162">30°</text><text x="222" y="162">45°</text><text x="284" y="162">60°</text>
    </g>
  </svg>
  <p class="chart-caption">DEGREES OF <span class="bold">FORWARD HEAD TILT</span></p>
  <p class="chart-axis-label">PRESSURE ON SPINR (LBS)</p>

  <svg class="pie" width="110" height="110" viewBox="0 0 110 110" role="img" aria-label="Pie chart of daily time spent on electronic devices">
    <circle cx="55" cy="55" r="54" fill="#e4e4e4"/>
    <circle cx="55" cy="55" r="49" fill="#8dc63f"/>
    <path d="M55 55 L55 6 A49 49 0 0 1 83.1 95.1 Z" fill="#0a72c0"/>
  </svg>
  <div class="screen-time">
    <p class="screen-time__lead">THE AVERAGE PERSON SPENDS</p>
    <p class="screen-time__hours">8-10 HOURS PER DAY</p>
    <p class="screen-time__tail">USING <span class="accent">ELECTRONIC DEVICES</span></p>
  </div>

  <p class="message">
    <span class="accent">CHIROPRACTIC CARE CAN HELP</span> CORRECT<br>
    AND PREVENT THESE PROBLEMS BY <span class="accent">RESTORING</span><br>
    AND <span class="accent">MAINTAINING</span><br>
    <span class="accent">PROPER ALIGNMENT</span> OF THE <span class="accent">NECK</span>
  </p>

  <div class="doctor-band">DR. SAMUEL WHITFORD</div>
  <p class="location">NOW IN BAYWATER AT : 42 HARBOUR RD.</p>
  <div class="offer">50% OFF INITIAL CONSULTATION</div>
  <p class="booking">IF YOU BOOK ONLINE AT <span class="booking__url">WWW.SPINEEASECLINIC.COM.AU</span></p>
  <div class="option">*CHOOSE <span class="option__key">"TECH NECK"</span> OPTION</div>
</main>
</body>
</html>
```